Willowbend Pharmacy Business Cards

I need a business card design and or template. Needs to convey a softer feel along with health and wellness. Please see attached logo and color scheme.

Industry/Entity Type

Pharmacy

Colors

Designer to choose colors to be used in the design.

Requirements
Must have
• I've added a second NEW colored logo I think I am going to go with the blue green logo.
• Needs to have the colors and feel of the logo attached.
• Darrel Quimby
• Pharmacy Manager
• willowbendpharmacy.example

```html
<!DOCTYPE html>
<html lang="en">
<head>
<meta charset="utf-8">
<title>Willowbend Pharmacy Business Cards</title>
<link rel="stylesheet" href="https://fonts.googleapis.com/css2?family=Montserrat:wght@400;500;600;700&display=swap">
<style>
  :root {
    --page-bg: #2b2b2b;
    --card-white: #ffffff;
    --brand-blue: #2e9fd6;
    --brand-blue-deep: #1f86bf;
    --brand-blue-light: #4fb6e6;
    --brand-green: #7aa92e;
    --brand-green-text: #8cc63f;
    --ink: #1e1e1e;
    --ink-soft: #555555;
  }
  * { box-sizing: border-box; margin: 0; padding: 0; }
  html, body {
    width: 1200px; height: 997px; overflow: hidden;
    background: var(--page-bg);
    font-family: "Montserrat", Arial, sans-serif;
  }
  .canvas {
    position: relative; width: 1200px; height: 997px;
  }
  .card {
    position: absolute; left: 320px; width: 560px; height: 320px;
    border-radius: 16px; overflow: hidden;
    box-shadow: 0 12px 30px rgba(0,0,0,.45);
  }
  /* Back of card */
  .card-back { top: 150px; }
  .card-back .backdrop {
    position: absolute; inset: 0;
    background: linear-gradient(135deg, var(--brand-blue-light) 0%, var(--brand-blue) 50%, var(--brand-blue-deep) 100%);
  }
  .back-brand {
    position: absolute; left: 0; right: 0; top: 108px;
    display: flex; align-items: center; justify-content: center; gap: 18px;
  }
  .back-brand .mark {
    width: 56px; height: 56px; border-radius: 50%; background: #fff;
  }
  .back-brand .wordmark { color: #fff; }
  .back-brand .name {
    font-size: 42px; font-weight: 700; letter-spacing: .5px; line-height: 1;
  }
  .back-brand .rule {
    width: 150px; height: 2px; background: #fff; margin-top: 10px;
  }
  .back-brand .sub {
    font-size: 14px; font-weight: 500; letter-spacing: 3px; text-align: right; margin-top: -10px;
  }
  .back-url {
    position: absolute; right: 34px; bottom: 26px;
    color: #fff; font-size: 13px; letter-spacing: .8px;
  }
  /* Front of card */
  .card-front { top: 527px; background: var(--card-white); }
  .front-brand {
    position: absolute; right: 30px; top: 26px;
    display: flex; align-items: center; gap: 8px;
  }
  .front-brand .mark {
    width: 30px; height: 30px; border-radius: 50%; background: var(--brand-blue);
  }
  .front-brand .name {
    font-size: 19px; font-weight: 700; color: var(--ink-soft); line-height: 1;
  }
  .front-brand .rule {
    width: 80px; height: 2px; background: var(--brand-green-text); margin-top: 4px;
  }
  .front-brand .sub {
    font-size: 8px; font-weight: 600; letter-spacing: 1.6px; color: var(--brand-blue); text-align: right; margin-top: -5px;
  }
  .person { position: absolute; left: 34px; top: 92px; }
  .person .name {
    font-size: 18px; font-weight: 700; color: var(--brand-green-text);
  }
  .person .role {
    font-size: 10px; color: var(--ink); margin-top: 2px;
  }
  .address {
    position: absolute; left: 34px; top: 150px;
    font-size: 11.5px; font-weight: 700; color: var(--brand-green-text); line-height: 1.6;
  }
  .contacts {
    position: absolute; left: 34px; top: 212px; list-style: none;
  }
  .contacts li {
    display: flex; align-items: center; gap: 10px;
    font-size: 12.5px; color: var(--ink); height: 24px;
  }
  .contacts .icon { width: 16px; height: 16px; flex: none; }
  .swoosh { position: absolute; left: 0; bottom: 0; width: 560px; height: 140px; }
</style>
</head>
<body>
<main class="canvas">

  <section class="card card-back" aria-label="Card back">
    <div class="backdrop" role="img" aria-label="Soft blue faceted background pattern"></div>
    <div class="back-brand">
      <span class="mark"></span>
      <div class="wordmark">
        <div class="name">Willowbend</div>
        <div class="rule"></div>
        <div class="sub">PHARMACY</div>
      </div>
    </div>
    <div class="back-url">www.willowbendpharmacy.example</div>
  </section>

  <section class="card card-front" aria-label="Card front">
    <div class="front-brand">
      <span class="mark"></span>
      <div class="wordmark">
        <div class="name">Willowbend</div>
        <div class="rule"></div>
        <div class="sub">PHARMACY</div>
      </div>
    </div>

    <div class="person">
      <div class="name">Darrel Quimby</div>
      <div class="role">Pharmacy Manager</div>
    </div>

    <address class="address" style="font-style:normal">
      4815 Alder Lane Suite,<br>
      210 Maplewood ON K0A 1B2
    </address>

    <ul class="contacts">
      <li>
        <svg class="icon" viewBox="0 0 16 16"><circle cx="8" cy="8" r="8" fill="var(--brand-green)"/><path d="M5 5.5c0 3 2.5 5.5 5.5 5.5l.8-1.4-1.6-.9-.7.7c-1-.4-1.6-1-2-2l.7-.7-.9-1.6z" fill="#fff"/></svg>
        +100 55 5012846
      </li>
      <li>
        <svg class="icon" viewBox="0 0 16 16"><circle cx="8" cy="8" r="8" fill="var(--brand-green)"/><rect x="5.5" y="3.8" width="5" height="8.4" rx="1" fill="none" stroke="#fff" stroke-width="1.1"/><circle cx="8" cy="10.6" r=".6" fill="#fff"/></svg>
        +100 555 - 01937
      </li>
      <li>
        <svg class="icon" viewBox="0 0 16 16"><circle cx="8" cy="8" r="8" fill="var(--brand-green)"/><rect x="4.2" y="5.3" width="7.6" height="5.4" fill="none" stroke="#fff" stroke-width="1.1"/><path d="M4.2 5.3 8 8.3l3.8-3" fill="none" stroke="#fff" stroke-width="1.1"/></svg>
        darrel418@willowbend.example
      </li>
    </ul>

    <svg class="swoosh" viewBox="0 0 560 140" preserveAspectRatio="none" aria-hidden="true">
      <path d="M250 140 C 380 95 480 50 560 10 L560 28 C 470 70 370 110 270 140 Z" fill="var(--brand-blue)"/>
      <path d="M0 110 C 220 120 420 80 560 34 L560 140 L0 140 Z" fill="var(--brand-green)"/>
    </svg>
  </section>

</main>
</body>
</html>
```